Restoration Business Cards

I’m in the water damage restoration industry and we specialize in water, mold, fire and restoration. I’m looking to get new business cards.

Business cards must have my logo with the letters

K-7 Max
Emergency Restoration

Owner
Marcus Whitlow
(555)482-7160
k7maxwork@mailtrove.net
https://www.k7maxwork.net
Lic #4870652 D-34 F
•Water •Mold •Fire •Restoration
OWTFB Certified #27158804

Add an QR code

```html
<!DOCTYPE html>
<html lang="en">
<head>
<meta charset="utf-8">
<title>K-7 Max Emergency Restoration – Business Cards</title>
<link rel="stylesheet" href="https://fonts.googleapis.com/css2?family=Montserrat:wght@500;700&family=Open+Sans:wght@400;600&display=swap">
<style>
  :root {
    --stage: #2b2c2f;
    --card-white: #ffffff;
    --card-black: #222325;
    --blue: #1f6fe0;
    --blue-light: #4f9bf2;
    --gold: #c9a462;
    --gold-dark: #9a6a24;
    --ink: #555555;
    --muted: #777777;
  }
  * { box-sizing: border-box; margin: 0; padding: 0; }
  html, body { width: 1200px; height: 952px; overflow: hidden; }
  body {
    background: var(--stage);
    font-family: "Open Sans", Arial, sans-serif;
    display: flex;
    align-items: center;
    justify-content: center;
    gap: 40px;
  }
  .card {
    width: 540px;
    height: 309px;
    position: relative;
    overflow: hidden;
    box-shadow: 0 14px 30px rgba(0,0,0,.45);
  }

  /* Front */
  .card-front { background: var(--card-white); }
  .brand {
    position: absolute;
    left: 34px;
    top: 30px;
    display: flex;
    align-items: center;
    gap: 12px;
    font-family: "Montserrat", Arial, sans-serif;
    font-weight: 700;
    color: var(--blue);
  }
  .brand-dot {
    width: 38px; height: 38px;
    border-radius: 50%;
    background: var(--blue);
  }
  .brand-name { font-size: 26px; line-height: 1; }
  .brand-tag { font-size: 10px; letter-spacing: 1.6px; text-transform: uppercase; margin-top: 4px; }
  .contacts {
    position: absolute;
    left: 34px;
    top: 122px;
    list-style: none;
    font-size: 12px;
    color: var(--ink);
  }
  .contacts li { display: flex; align-items: center; gap: 9px; margin-bottom: 7px; }
  .icon {
    width: 17px; height: 17px;
    border-radius: 3px;
    background: var(--blue);
    display: flex; align-items: center; justify-content: center;
  }
  .credentials {
    position: absolute;
    left: 34px;
    top: 218px;
    font-size: 11.5px;
    line-height: 1.6;
  }
  .credentials .label { color: var(--blue); }
  .credentials .value { color: var(--gold-dark); }
  .person {
    position: absolute;
    right: 70px;
    top: 150px;
    text-align: right;
  }
  .person-name {
    font-family: "Montserrat", Arial, sans-serif;
    font-weight: 500;
    font-size: 22px;
    color: var(--blue);
    letter-spacing: .5px;
    text-transform: uppercase;
  }
  .person-name strong { font-weight: 700; }
  .person-title {
    font-size: 14px;
    color: var(--muted);
    letter-spacing: 1px;
    margin-top: 2px;
  }
  .corner-block {
    position: absolute;
    right: 0; bottom: 0;
    width: 52px; height: 52px;
    background: linear-gradient(135deg, var(--blue-light), var(--blue));
  }

  /* Back */
  .card-back { background: var(--card-black); }
  .back-brand {
    position: absolute;
    left: 0; right: 0;
    top: 58px;
    text-align: center;
    font-family: "Montserrat", Arial, sans-serif;
    font-weight: 700;
    color: var(--blue-light);
  }
  .back-brand .brand-name { font-size: 46px; }
  .back-brand .brand-tag { font-size: 14px; letter-spacing: 3px; margin-top: 8px; }
  .service-band {
    position: absolute;
    left: 0; right: 0;
    top: 198px;
    height: 34px;
    background: linear-gradient(90deg, var(--gold), #e0c184 40%, var(--gold-dark));
    color: #ffffff;
    font-weight: 600;
    font-size: 15px;
    letter-spacing: 1.5px;
    display: flex;
    align-items: center;
    justify-content: center;
    gap: 16px;
  }
</style>
</head>
<body>

<section class="card card-front" aria-label="Business card front">
  <div class="brand">
    <span class="brand-dot"></span>
    <div>
      <div class="brand-name">K-7 Max</div>
      <div class="brand-tag">Emergency Restoration</div>
    </div>
  </div>

  <ul class="contacts">
    <li>
      <span class="icon"><svg width="11" height="11" viewBox="0 0 24 24"><path fill="#fff" d="M6.6 10.8a15 15 0 0 0 6.6 6.6l2.2-2.2a1 1 0 0 1 1-.25 11.4 11.4 0 0 0 3.6.6 1 1 0 0 1 1 1V20a1 1 0 0 1-1 1A17 17 0 0 1 3 4a1 1 0 0 1 1-1h3.5a1 1 0 0 1 1 1c0 1.25.2 2.45.6 3.6a1 1 0 0 1-.25 1z"/></svg></span>
      (555)482-7160
    </li>
    <li>
      <span class="icon"><svg width="11" height="11" viewBox="0 0 24 24"><path fill="none" stroke="#fff" stroke-width="2.4" d="M3 6h18v12H3z M3 6l9 7 9-7"/></svg></span>
      k7maxwork@mailtrove.net
    </li>
    <li>
      <span class="icon"><svg width="11" height="11" viewBox="0 0 24 24"><path fill="#fff" d="M12 2a7 7 0 0 0-7 7c0 5 7 13 7 13s7-8 7-13a7 7 0 0 0-7-7zm0 9.5A2.5 2.5 0 1 1 12 6.5a2.5 2.5 0 0 1 0 5z"/></svg></span>
      www.k7maxwork.net
    </li>
  </ul>

  <div class="credentials">
    <div><span class="label">Lic</span> <span class="value">#4870652 D-34 F</span></div>
    <div><span class="label">OWTFB Certified</span> <span class="value">#27158804</span></div>
  </div>

  <div class="person">
    <div class="person-name">Marcus <strong>Whitlow</strong></div>
    <div class="person-title">Owner</div>
  </div>

  <div class="corner-block"></div>
</section>

<section class="card card-back" aria-label="Business card back">
  <div class="back-brand">
    <div class="brand-name">K-7 Max</div>
    <div class="brand-tag">Emergency Restoration 24/7</div>
  </div>
  <div class="service-band">
    <span>• Water</span><span>• Mold</span><span>• Fire</span><span>• Restoration</span>
  </div>
</section>

</body>
</html>
```